Banner ads for VL that work with same theme as below banners

Love the banner ads below. Need more with attached photos. But use the same wording, font as in below banner ads. Should be VL size 1200/627 so I can use for Trovique and VL. Looking for great ads to use as VL ads. We do lots of ads so it will be worth your time to enter this contest you will be rewarded with a ton of work. Need several banner ads that work together. So maybe 1 of the dresses, 1 of the sweater, 1 of the leggings, 1 of the jacket

Target Market(s)

Women 24-45

Industry/Entity Type

Fashion

Requirements
Must have
• Banner ads that work for VL and Trovique
Nice to have
• Several options to choose from
Should not have
• not sure

```html
<!DOCTYPE html>
<html lang="en">
<head>
<meta charset="utf-8">
<title>Exotic Leggings Collection</title>
<link rel="stylesheet" href="https://fonts.googleapis.com/css2?family=Courgette&family=Libre+Baskerville&family=Open+Sans:wght@400;700&display=swap">
<style>
  :root {
    --bg-light: #f1f2f9;
    --bg-mid: #d9dcee;
    --bg-edge: #b9bdd8;
    --band-light: #f6f7fc;
    --band-shadow: rgba(120, 124, 160, 0.35);
    --ink: #0b0b12;
    --script: #ffffff;
    --script-shadow: rgba(60, 62, 90, 0.55);
    --navy: #1c2138;
    --navy-deep: #0e1222;
    --lace: #e7e8f0;
    --button-top: #ffffff;
    --button-mid: #d3d5df;
    --button-bottom: #8e91a2;
    --button-ink: #2a2b33;
  }
  * { margin: 0; padding: 0; box-sizing: border-box; }
  html, body { width: 1200px; height: 627px; overflow: hidden; }
  body { background: var(--bg-mid); }

  .banner {
    position: relative;
    width: 1200px;
    height: 627px;
    overflow: hidden;
    background:
      radial-gradient(ellipse 700px 420px at 560px 300px, var(--bg-light) 0%, rgba(241,242,249,0) 100%),
      linear-gradient(180deg, var(--bg-mid) 0%, var(--bg-light) 45%, var(--bg-edge) 100%);
  }

  .ornament {
    position: absolute;
    border-radius: 50%;
  }
  .ornament--top-right {
    right: -60px; top: -80px; width: 520px; height: 360px;
    background: radial-gradient(closest-side, rgba(170,174,205,0.55), rgba(170,174,205,0));
  }
  .ornament--bottom-left {
    left: 120px; bottom: -90px; width: 360px; height: 300px;
    background: radial-gradient(closest-side, rgba(170,174,205,0.5), rgba(170,174,205,0));
  }

  .band {
    position: absolute;
    left: 250px; right: 0;
    top: 255px; height: 60px;
    background: linear-gradient(180deg, var(--band-light) 0%, #eceef8 100%);
    box-shadow: 0 -2px 4px var(--band-shadow), 0 3px 6px var(--band-shadow);
  }

  .product-photo {
    position: absolute;
    left: 30px; top: 0;
    width: 255px; height: 607px;
    border-radius: 40px 40px 20px 20px;
    background: linear-gradient(180deg, var(--lace) 0%, var(--navy) 8%, var(--navy-deep) 55%, var(--navy) 92%, #d8b8a8 100%);
  }

  .headline {
    position: absolute;
    left: 800px; width: 340px;
    top: 180px;
    text-align: center;
  }
  .headline__script {
    display: block;
    font-family: "Courgette", cursive;
    color: var(--script);
    font-size: 50px;
    line-height: 1;
    text-shadow: 1px 2px 3px var(--script-shadow), 0 0 1px var(--script-shadow);
  }
  .headline__main {
    display: block;
    font-family: "Libre Baskerville", serif;
    color: var(--ink);
    font-size: 56px;
    letter-spacing: 1px;
    line-height: 1;
    margin-top: 28px;
  }
  .headline__script--lower { margin-top: 18px; }

  .cta {
    position: absolute;
    left: 812px; top: 458px;
    width: 304px; height: 46px;
    border-radius: 23px;
    background: linear-gradient(180deg, var(--button-top) 0%, var(--button-mid) 50%, var(--button-bottom) 100%);
    box-shadow: 0 2px 4px rgba(60,62,90,0.4), inset 0 1px 0 #fff;
    display: flex; align-items: center; justify-content: center;
    font-family: "Open Sans", sans-serif;
    font-size: 25px;
    color: var(--button-ink);
    text-decoration: none;
    letter-spacing: 0.3px;
  }
  .cta strong { font-weight: 700; }
  .cta span { font-weight: 400; margin: 0 8px; }
</style>
</head>
<body>
  <main class="banner">
    <div class="ornament ornament--top-right" role="img" aria-label="Faint floral swirl decoration"></div>
    <div class="ornament ornament--bottom-left" role="img" aria-label="Faint floral swirl decoration"></div>

    <div class="band"></div>

    <div class="product-photo" role="img" aria-label="Model wearing navy leggings with white lace-print bands, standing barefoot"></div>

    <h1 class="headline">
      <span class="headline__script">Exotic</span>
      <span class="headline__main">LEGGINGS</span>
      <span class="headline__script headline__script--lower">Collection</span>
    </h1>

    <a class="cta" href="#"><strong>GET</strong><span>THEM</span><strong>NOW</strong></a>
  </main>
</body>
</html>
```